Veteran Owned General Contractor needs Bold New Business Cards

We are a service disabled veteran owned small business. We're a general contractor that specializes in excavation, underground utilities, site work, land clearing and demolition. We would like a fresh, simple, bold, new look for our business cards. We're open to ideas! We'd like to incorporate the following information on the card:

Company Name & Logo, Name of Person, Job Title, Office Phone, Fax, Cell Phone, Email Address, Website, SDVOSB

Our logo is included. We look forward to your thoughts.

Thank you!
Updates

Reason: Hello Due to the overwhelming response to this project, we are extending the deadline one time to allow for improved communication and feedback with the top candidates. We would like to thank everyone for their hard work and exceptional creativity! Thank you

Industry/Entity Type

Business

Contact Information for Business Card

Font styles to use
Sans Serif

Requirements
Nice to have
• As we are a veteran owned company, it would be nice to incorporate an American flag into the design. Maybe on the back?

```html
<!DOCTYPE html>
<html lang="en">
<head>
<meta charset="utf-8">
<title>Kestrel9 Inc — Business Card</title>
<link rel="stylesheet" href="https://fonts.googleapis.com/css2?family=Mulish:wght@400;800&display=swap">
<style>
  :root {
    --lime: #5fe60f;
    --band-dark: #15a300;
    --band-top: #17a400;
    --band-bottom: #a4f300;
    --ink: #111111;
    --icon-grey: #6e6e6e;
    --mark-dark: #1d1d1d;
    --left-bg-start: #ffffff;
    --left-bg-end: #dcdcdc;
    --right-bg-start: #ececec;
    --right-bg-end: #bababa;
  }
  html, body { margin: 0; padding: 0; overflow: hidden; background: #ffffff; }
  .card {
    position: relative;
    width: 1200px;
    height: 683px;
    overflow: hidden;
    font-family: "Mulish", sans-serif;
    color: var(--ink);
    background: linear-gradient(100deg, var(--left-bg-start) 0%, var(--left-bg-end) 45%, var(--right-bg-start) 55%, var(--right-bg-end) 100%);
  }
  .bands { position: absolute; inset: 0; }
  .company-mark {
    position: absolute;
    left: 195px; top: 121px;
    width: 108px; height: 106px;
    background: var(--mark-dark);
    border-radius: 14px;
  }
  .company-name {
    position: absolute;
    left: 46px; top: 262px;
    width: 404px;
    margin: 0;
    font-weight: 800;
    font-size: 50px;
    line-height: 1;
    letter-spacing: 1px;
    color: var(--lime);
    white-space: nowrap;
    text-align: center;
  }
  .certification {
    position: absolute;
    left: 107px; top: 346px;
    margin: 0;
    font-size: 23px;
    letter-spacing: 26px;
  }
  .company-contacts {
    position: absolute;
    left: 46px; top: 440px;
    margin: 0; padding: 0;
    list-style: none;
  }
  .company-contacts li {
    display: flex;
    align-items: flex-start;
    gap: 14px;
    font-size: 38px;
    line-height: 44px;
    height: 63px;
  }
  .company-contacts svg { flex: none; width: 44px; height: 44px; margin-top: 0; }
  .person {
    position: absolute;
    left: 795px; top: 178px;
  }
  .person-name {
    margin: 0;
    font-weight: 800;
    font-size: 53px;
    line-height: 1;
    letter-spacing: 1px;
  }
  .person-title {
    margin: 22px 0 0;
    font-size: 27px;
    line-height: 1;
  }
  .person-contacts { margin: 18px 0 0; padding: 0; list-style: none; }
  .person-contacts li { display: flex; align-items: center; gap: 14px; }
  .person-contacts .mobile { font-size: 38px; height: 54px; }
  .person-contacts .mobile svg { width: 40px; height: 46px; }
  .person-contacts .email { font-size: 23px; margin-top: 14px; margin-left: -6px; }
  .person-contacts .email svg { width: 44px; height: 30px; }
</style>
</head>
<body>
<main class="card">
  <svg class="bands" width="1200" height="683" viewBox="0 0 1200 683" aria-hidden="true">
    <defs>
      <linearGradient id="band-glow" x1="0" y1="0" x2="0" y2="1">
        <stop offset="0" stop-color="var(--band-top)"/>
        <stop offset="1" stop-color="var(--band-bottom)"/>
      </linearGradient>
    </defs>
    <polygon points="422,0 711,0 831,683 547,683" fill="var(--band-dark)"/>
    <polygon points="422,0 630,0 739,683 547,683" fill="url(#band-glow)"/>
  </svg>

  <section class="company">
    <div class="company-mark" aria-hidden="true"></div>
    <h1 class="company-name">KESTREL9 INC</h1>
    <p class="certification">SVDOSB</p>
    <ul class="company-contacts">
      <li>
        <svg viewBox="0 0 44 44" aria-hidden="true"><rect width="44" height="44" rx="7" fill="var(--lime)"/><path d="M15 9c2 0 4 5 4 7s-3 2-3 4 4 8 6 8 2-3 4-3 6 2 6 4-2 5-5 5C17 34 10 22 10 15c0-3 3-6 5-6z" fill="#fff"/></svg>
        <span>555-20-37</span>
      </li>
      <li>
        <svg viewBox="0 0 44 44" aria-hidden="true"><rect x="11" y="3" width="22" height="10" fill="var(--lime)"/><rect x="2" y="14" width="40" height="18" rx="4" fill="var(--lime)"/><rect x="10" y="26" width="24" height="16" fill="var(--lime)" stroke="#fff" stroke-width="2"/><rect x="14" y="31" width="16" height="2" fill="#fff"/><rect x="14" y="36" width="16" height="2" fill="#fff"/></svg>
        <span>555-20-37</span>
      </li>
      <li>
        <svg viewBox="0 0 44 44" aria-hidden="true"><polygon points="22,3 43,18 1,18" fill="var(--lime)"/><rect x="6" y="20" width="32" height="3" fill="var(--lime)"/><rect x="8" y="23" width="4" height="19" fill="var(--lime)"/><rect x="32" y="23" width="4" height="19" fill="var(--lime)"/></svg>
        <span>ASHFORD, MA 01790<br>USA</span>
      </li>
    </ul>
  </section>

  <section class="person">
    <h2 class="person-name">DANIEL BROOKS</h2>
    <p class="person-title">PROJECT MANAGER</p>
    <ul class="person-contacts">
      <li class="mobile">
        <svg viewBox="0 0 40 46" aria-hidden="true"><rect x="6" y="1" width="28" height="44" rx="5" fill="var(--icon-grey)"/><rect x="10" y="7" width="20" height="30" fill="#d9d9d9"/></svg>
        <span>555-20-37-08</span>
      </li>
      <li class="email">
        <svg viewBox="0 0 44 30" aria-hidden="true"><rect width="44" height="30" fill="var(--icon-grey)"/><polyline points="0,0 22,17 44,0" fill="none" stroke="#e3e3e3" stroke-width="3"/></svg>
        <span>Daniel.Brooks@KESTREL9.com</span>
      </li>
    </ul>
  </section>
</main>
</body>
</html>
```